Tarn Structural Approval Standards Private Assessors

Professional Construction Consultancy Company Business Card - must keep logo colours see images below - examples have been added from my last competition - please see them as examples only!

Target Market(s)

Home Builders

Industry/Entity Type

Construction

Contact Information for Business Card

See "must haves"

Font styles to use
Sans Serif

Colors
ffffff
add136
000000

Requirements
Must have
• Daniel Moravi
• Director
• Phone: 0431 587 219
• Address: 7 Tarrunga Rd,
• Hallworth Vale, SA, 5091
• Email: tarnassessors@mailbox-example.com
• Website: www.tarnassessors-example.com.au
• Facebook: Tarn Structural Approval Standards
Nice to have
• Side 1: full logo
• Side 2: company details
Should not have
• hard to read
• must be clear and professional

```html
<!DOCTYPE html>
<html lang="en">
<head>
<meta charset="utf-8">
<title>Tarn Structural Approval Standards – Business Card</title>
<link href="https://fonts.googleapis.com/css2?family=Arimo:wght@400;700&display=swap" rel="stylesheet">
<style>
  :root {
    --green: #a0c83e;
    --black: #141517;
    --white: #ffffff;
    --ink: #1b1b1b;
    --bg-light: #f0f0f2;
    --bg-dark: #dcdcdf;
  }
  * { margin: 0; padding: 0; box-sizing: border-box; }
  html, body { width: 1200px; height: 1000px; overflow: hidden; }
  body {
    font-family: "Arimo", Arial, sans-serif;
    background: radial-gradient(ellipse at 50% 30%, var(--bg-light) 0%, var(--bg-dark) 100%);
    position: relative;
  }
  .card {
    position: absolute;
    left: 254px;
    width: 690px;
    height: 408px;
    border-radius: 28px;
    overflow: hidden;
    box-shadow: 4px 6px 10px rgba(0,0,0,0.25);
  }
  /* Front side */
  .card-front { top: 80px; background: var(--black); }
  .front-brand {
    position: absolute;
    left: 0; right: 0; top: 150px;
    text-align: center;
    color: var(--green);
    font-weight: 700;
  }
  .front-brand .brand-name {
    font-size: 30px;
    line-height: 36px;
    letter-spacing: 0.5px;
    text-transform: uppercase;
  }
  .front-brand .brand-sub {
    margin-top: 8px;
    font-size: 19px;
    letter-spacing: 4.5px;
    text-transform: uppercase;
  }
  .front-web {
    position: absolute;
    left: 0; right: 0; top: 360px;
    display: flex;
    align-items: center;
    justify-content: center;
    gap: 10px;
    color: var(--white);
    font-size: 16px;
  }
  .front-web .rule { width: 130px; height: 1px; }
  .front-web .rule-left { background: linear-gradient(to right, transparent, #d0d0d0); }
  .front-web .rule-right { background: linear-gradient(to left, transparent, #d0d0d0); }
  .front-web .domain { color: var(--green); }

  /* Back side */
  .card-back { top: 522px; background: var(--white); }
  .back-wave { position: absolute; left: 0; top: 0; width: 690px; height: 408px; }
  .holder { position: absolute; left: 36px; top: 34px; }
  .holder-name { color: var(--green); font-weight: 700; font-size: 24px; }
  .holder-role { color: var(--ink); font-size: 16px; margin-top: 4px; text-transform: uppercase; }
  .back-brand {
    position: absolute;
    right: 48px; top: 36px;
    text-align: right;
    color: var(--green);
    font-weight: 700;
    text-transform: uppercase;
  }
  .back-brand .brand-name { font-size: 15px; line-height: 18px; }
  .back-brand .brand-sub { font-size: 12px; letter-spacing: 2.6px; margin-top: 4px; }
  .contact { position: absolute; color: var(--ink); font-size: 18px; white-space: nowrap; }
  .address { left: 36px; top: 244px; line-height: 23px; }
  .contact-line { display: flex; align-items: center; gap: 7px; left: 36px; }
  .contact-line svg { flex: none; }
  .phone { top: 304px; }
  .email { top: 337px; }
  .social { top: 372px; font-size: 17px; }
  .web { left: auto; right: 26px; top: 372px; font-size: 16px; }
</style>
</head>
<body>

<section class="card card-front" aria-label="Card front">
  <div class="front-brand">
    <div class="brand-name">Tarn Structural<br>Approval Standards</div>
    <div class="brand-sub">Private Assessors</div>
  </div>
  <div class="front-web">
    <span class="rule rule-left"></span>
    <span>www.<span class="domain">tarnassessors-example</span>.com.au</span>
    <span class="rule rule-right"></span>
  </div>
</section>

<section class="card card-back" aria-label="Card back">
  <svg class="back-wave" viewBox="0 0 690 408" aria-hidden="true">
    <defs>
      <linearGradient id="swoosh" x1="0" y1="0" x2="1" y2="0">
        <stop offset="0" stop-color="#a0c83e" stop-opacity="0.9"/>
        <stop offset="1" stop-color="#a0c83e" stop-opacity="0"/>
      </linearGradient>
    </defs>
    <path d="M215,199 Q470,215 690,288 L690,296 Q470,222 215,199 Z" fill="url(#swoosh)"/>
    <path d="M0,200 Q260,180 690,302 L690,408 L0,408 Z" fill="var(--green)"/>
  </svg>

  <div class="holder">
    <div class="holder-name">Daniel Moravi</div>
    <div class="holder-role">Director</div>
  </div>

  <div class="back-brand">
    <div class="brand-name">Tarn Structural<br>Approval Standards</div>
    <div class="brand-sub">Private Assessors</div>
  </div>

  <div class="contact address">7 Tarrunga Rd,<br>Hallworth Vale, SA, 5091</div>

  <div class="contact contact-line phone">
    <svg width="17" height="17" viewBox="0 0 17 17" aria-hidden="true">
      <circle cx="8.5" cy="8.5" r="7.5" fill="none" stroke="#fff" stroke-width="1.3"/>
      <path d="M6,4.5 L7.5,6.5 L6.8,7.5 Q7.6,9.4 9.5,10.2 L10.5,9.5 L12.5,11 L11.5,12.5 Q7.5,12.5 4.5,7.5 Z" fill="#fff"/>
    </svg>
    <span>0431 587 219</span>
  </div>

  <div class="contact contact-line email">
    <svg width="18" height="14" viewBox="0 0 18 14" aria-hidden="true">
      <rect x="1" y="1.5" width="16" height="11" fill="none" stroke="#fff" stroke-width="1.3"/>
      <path d="M1,1.5 L9,8 L17,1.5" fill="none" stroke="#fff" stroke-width="1.3"/>
    </svg>
    <span>tarnassessors@mailbox-example.com</span>
  </div>

  <div class="contact contact-line social">
    <svg width="14" height="14" viewBox="0 0 14 14" aria-hidden="true">
      <rect x="0" y="0" width="14" height="14" rx="2" fill="#fff"/>
    </svg>
    <span>Tarn Structural Approval Standards</span>
  </div>

  <div class="contact contact-line web">
    <svg width="16" height="16" viewBox="0 0 17 17" aria-hidden="true">
      <circle cx="8.5" cy="8.5" r="7.5" fill="none" stroke="#fff" stroke-width="1.2"/>
      <ellipse cx="8.5" cy="8.5" rx="3.3" ry="7.5" fill="none" stroke="#fff" stroke-width="1.1"/>
      <path d="M1,8.5 H16 M2.5,4.8 H14.5 M2.5,12.2 H14.5" stroke="#fff" stroke-width="1.1"/>
    </svg>
    <span>www.tarnassessors-example.com.au</span>
  </div>
</section>

</body>
</html>
```